KDV by Moira Tallow - Scalp Micropigmentation

I need a wordpress site designed for me, can be based off a theme, I already have a logo and the press site ready to be created, I can provide a login for you. I will be able to update it myself with content I just need the layout done as Im having trouble with it. I want to be able to add pages as needed and have a gallery for my work.

Target Market(s)

customers

Coding

Coded - Design and coding required

Number of Pages Required

5+ page

Font styles to use
Sans Serif

Colors

Designer to choose colors to be used in the design.

Requirements
Must have
• my logo, wordpress, gallery
Should not have
• shopping cart

```html
<!DOCTYPE html>
<html lang="en">
<head>
<meta charset="utf-8">
<title>KDV by Moira Tallow – Scalp Micropigmentation</title>
<link href="https://fonts.googleapis.com/css2?family=Montserrat:wght@400;500;600;700&family=Open+Sans:wght@400;600;700&display=swap" rel="stylesheet">
<style>
:root{
  --bg:#f2f2f2;
  --white:#ffffff;
  --ink:#222222;
  --muted:#777777;
  --line:#d6d6d6;
  --blue:#4aa3df;
  --blue-band:#5aa8da;
  --hero-grey:#e4e4e4;
  --dark:#2a2a2a;
  --star:#f5c518;
}
*{margin:0;padding:0;box-sizing:border-box}
html,body{width:770px;height:1200px;overflow:hidden;background:var(--bg)}
body{position:relative;font-family:"Open Sans",Arial,sans-serif;color:var(--ink)}
.page{position:absolute;width:288px;background:var(--white);box-shadow:0 1px 6px rgba(0,0,0,.08);overflow:hidden}
.page--home{left:68px;top:66px;height:1068px}
.page--faq{left:414px;top:66px;height:605px}
section,header,footer{position:relative;width:100%}
.heading{font-family:"Montserrat",Arial,sans-serif;font-weight:400;letter-spacing:.2px}

/* header */
.site-header{height:27px;background:var(--white)}
.logo{position:absolute;left:27px;top:7px;width:41px;height:41px;background:var(--white);border:1px solid var(--ink);z-index:5;display:flex;flex-direction:column;align-items:center;justify-content:center}
.logo__name{font-family:"Montserrat",Arial,sans-serif;font-weight:600;font-size:11px;line-height:1}
.logo__by{font-family:"Montserrat",Arial,sans-serif;font-weight:600;font-size:2.6px;letter-spacing:.3px;margin-top:4px}
.nav{position:absolute;left:88px;top:12px;display:flex;gap:5.2px;font-size:4.2px}
.nav a{color:var(--ink);text-decoration:none}
.nav a.is-active{color:var(--blue)}
.nav svg{width:4px;height:4px;margin-top:.3px}

/* hero */
.hero{height:141px;background:var(--hero-grey)}
.hero--short{height:84px}
.hero__photo{position:absolute;right:0;top:0;width:150px;height:100%;background:linear-gradient(90deg,var(--hero-grey) 0%,#d6c7bc 35%,#c4a48e 60%,#d9d2cc 100%)}
.hero__arrow{position:absolute;top:50%;width:8px;height:10px;margin-top:-5px;background:#b9b9b9;display:flex;align-items:center;justify-content:center}
.hero__arrow svg{width:4px;height:5px}
.hero__title{position:absolute;left:27px;top:42px;font-family:"Montserrat",Arial,sans-serif;font-weight:500;font-size:13.4px;line-height:17px;letter-spacing:.4px;color:var(--ink)}
.hero__title--faq{top:35px;font-weight:700;font-size:17px}
.btn{display:inline-block;font-family:"Montserrat",Arial,sans-serif;font-weight:600;font-size:3.8px;letter-spacing:.3px;text-transform:uppercase}
.btn--solid{position:absolute;left:27px;top:98px;background:var(--blue);color:var(--white);padding:4.5px 6px}
.btn--outline{border:.6px solid var(--blue);color:var(--blue);padding:2.8px 4.5px}

/* welcome */
.welcome{height:122px}
.welcome__text{position:absolute;left:27px;top:26px;width:116px}
.welcome__title{font-size:8.4px;line-height:11.5px;text-transform:uppercase}
.small{font-size:3.4px;line-height:5.2px;color:var(--muted)}
.welcome__text .small{margin-top:6px}
.welcome__text .btn{margin-top:9px}
.welcome__divider{position:absolute;left:156px;top:40px;width:.6px;height:45px;background:var(--line)}
.features{position:absolute;left:175px;top:27px}
.feature{display:flex;align-items:center;height:20px;margin-bottom:4.8px}
.feature__icon{width:20px;height:20px;border-radius:50%;border:.6px solid var(--line);display:flex;align-items:center;justify-content:center;margin-right:6px}
.feature__icon svg{width:10px;height:10px}
.feature__title{font-family:"Montserrat",Arial,sans-serif;font-size:5px;text-transform:uppercase}
.feature .small{font-size:3px;line-height:4px;margin-top:1px}

/* services */
.services{height:147px;background:var(--dark)}
.services__bg{position:absolute;inset:0;background:linear-gradient(135deg,#1f1f1f 0%,#3a3a3a 45%,#5a4a40 75%,#2a2a2a 100%)}
.services__title{position:absolute;top:26px;width:100%;text-align:center;color:var(--white);font-size:8.6px;text-transform:uppercase}
.dotline{display:flex;align-items:center;justify-content:center;gap:2px}
.dotline i{display:block;width:1.4px;height:1.4px;border-radius:50%;background:currentColor}
.dotline b{display:block;width:10px;height:.5px;background:currentColor;margin:0 2px}
.services__rule{position:absolute;top:42px;width:100%;color:var(--white)}
.service-list{position:absolute;left:27px;top:60px;display:flex;gap:14px}
.service{width:69px;height:61px;border:1.6px solid var(--white);outline:.5px solid rgba(255,255,255,.5);outline-offset:1.2px;display:flex;flex-direction:column;align-items:center;justify-content:flex-end;padding-bottom:10px;color:var(--white)}
.service__mark{width:11px;height:11px;border:.8px solid var(--white);border-radius:50%;margin-bottom:6px}
.service__dots{margin-bottom:6px}
.service__dots i{width:1px;height:1px}
.service__name{font-weight:600;font-size:5px;line-height:6px}

/* transformations */
.transform{height:163px}
.transform__frame{position:absolute;left:120px;top:30px;width:141px;height:107px;border:.6px solid #bdbdbd}
.transform__photo{position:absolute;left:27px;top:42px;width:108px;height:82px;background:linear-gradient(90deg,#d8d2cd 0%,#cfc6bf 49.5%,#c8b7a9 50.5%,#d9d4cf 100%)}
.transform__label{position:absolute;top:5px;font-family:"Montserrat",Arial,sans-serif;font-weight:700;font-size:3.6px;color:#555}
.transform__text{position:absolute;left:147px;top:47px;width:104px}
.transform__text h2{font-size:8.6px;text-transform:uppercase}
.transform__text .small{margin-top:6px;font-size:3.2px;line-height:5px}
.transform__text .btn{margin-top:7px}

/* testimonials */
.testimonials{height:129px;background:var(--blue-band)}
.testimonials h2{position:absolute;top:22px;width:100%;text-align:center;color:var(--white);font-size:8.6px;text-transform:uppercase}
.round-arrow{position:absolute;width:10px;height:10px;border-radius:50%;border:.6px solid currentColor;display:flex;align-items:center;justify-content:center}
.round-arrow svg{width:3px;height:4px}
.testimonials .round-arrow{top:73px;color:var(--white)}
.cards{position:absolute;left:27px;top:48px;display:flex;gap:7px}
.card{position:relative;width:74px;height:60px;border:.6px solid rgba(255,255,255,.85);text-align:center;color:var(--white);padding:16px 5px 0}
.card__avatar{position:absolute;left:50%;top:-10px;width:19px;height:19px;margin-left:-9.5px;border-radius:50%;border:1px solid var(--white);background:#b79a86}
.card p{font-size:2.9px;line-height:4px;opacity:.9}
.card__name{font-weight:700;font-size:4.2px;margin-top:5px}
.stars{display:flex;justify-content:center;gap:.6px;margin-top:4px}
.stars svg{width:4px;height:4px}

/* gallery */
.gallery{height:130px}
.gallery h2{position:absolute;top:27px;width:100%;text-align:center;font-size:8.6px;text-transform:uppercase}
.gallery__row{position:absolute;left:27px;top:49px;display:flex;gap:2.5px}
.gallery__item{width:57px;height:49px}
.gallery .round-arrow{top:69px;color:#777}

/* contact */
.contact{height:130px;background:linear-gradient(90deg,#7b7674 0%,#86807d 55%,#a5a09d 100%)}
.contact__photo{position:absolute;right:0;top:0;width:120px;height:100%;background:linear-gradient(90deg,rgba(134,128,125,0) 0%,#6e6562 40%,#4a4442 70%,#a29d9a 100%)}
.contact h2{position:absolute;left:27px;top:26px;color:var(--white);font-size:8.4px;text-transform:uppercase}
.form{position:absolute;left:27px;top:46px;width:133px}
.form__row{display:flex;gap:2px;margin-bottom:3px}
.field{flex:1;height:7px;background:var(--white);font-size:2.8px;color:#999;padding:1.8px 3px;line-height:3px}
.field--area{height:18px;flex:none;width:100%}
.form__submit{position:absolute;right:0;top:47px;background:var(--blue);color:var(--white);font-family:"Montserrat",Arial,sans-serif;font-weight:700;font-size:3.2px;padding:2.5px 4.5px;text-transform:uppercase}

/* footer */
.site-footer{height:79px;text-align:center;color:var(--muted)}
.social{position:absolute;top:20px;width:100%;display:flex;justify-content:center;gap:2.5px}
.social span{width:11px;height:11px;border-radius:50%;border:.6px solid #9fb9cc}
.footer__contact{position:absolute;top:44px;width:100%;display:flex;justify-content:center;gap:3px;font-size:3.2px;align-items:center}
.footer__contact svg{width:3.5px;height:3.5px;margin-right:1px;vertical-align:-.5px}
.footer__links{position:absolute;top:53px;width:100%;font-size:3.2px;display:flex;justify-content:center;gap:4px}
.copyright{position:absolute;top:62px;width:100%;font-size:3.2px}
.site-footer--faq{height:76px}
.site-footer--faq .social{top:22px}
.site-footer--faq .footer__contact{top:45px}

/* faq */
.faq{height:288px}
.faq h2{position:absolute;top:24px;width:100%;text-align:center;font-family:"Montserrat",Arial,sans-serif;font-weight:600;font-size:9px;text-transform:uppercase}
.faq__list{position:absolute;left:27px;top:46px;width:235px}
.faq__item{position:relative;height:10.4px;margin-bottom:5px;border:.6px solid var(--line);padding-left:15px;font-size:4.2px;line-height:9.4px;color:#333;white-space:nowrap}
.faq__toggle{position:absolute;left:-.6px;top:-.6px;width:10.4px;height:10.4px;background:#555;display:flex;align-items:center;justify-content:center}
.faq__toggle svg{width:5px;height:5px}
.faq__item.is-open{height:24px;border-top:none;border-left:none}
.faq__item.is-open .faq__toggle{background:var(--blue)}
.faq__answer{font-size:3px;line-height:4px;color:var(--muted);margin-top:1px}
</style>
</head>
<body>

<div class="page page--home">
  <header class="site-header">
    <div class="logo"><span class="logo__name">KDV</span><span class="logo__by">BY MOIRA TALLOW</span></div>
    <nav class="nav">
      <a class="is-active">Home</a><a>About</a><a>Treatments</a><a>Gallery</a><a>Training</a><a>Transformations</a><a>Blog</a><a>Contact</a>
      <svg viewBox="0 0 10 10"><circle cx="4" cy="4" r="3" fill="none" stroke="#222" stroke-width="1.6"/><line x1="6.2" y1="6.2" x2="9" y2="9" stroke="#222" stroke-width="1.8"/></svg>
    </nav>
  </header>

  <section class="hero">
    <div class="hero__photo" role="img" aria-label="Man with a shaved head looking down, half of the scalp showing the pigmented hairline"></div>
    <div class="hero__arrow" style="left:0"><svg viewBox="0 0 4 6"><path d="M3 0.5 1 3 3 5.5" fill="none" stroke="#fff" stroke-width=".9"/></svg></div>
    <div class="hero__arrow" style="right:0"><svg viewBox="0 0 4 6"><path d="M1 0.5 3 3 1 5.5" fill="none" stroke="#fff" stroke-width=".9"/></svg></div>
    <h1 class="hero__title">SCALP<br>MICRO<br>PIGMENTATION</h1>
    <a class="btn btn--solid">Get free consultation</a>
  </section>

  <section class="welcome">
    <div class="welcome__text">
      <h2 class="heading welcome__title">Welcome to scalp<br>micro pigmentation</h2>
      <p class="small">Our studio restores the look of a full, natural hairline with careful, lasting pigment work tailored to you.</p>
      <a class="btn btn--outline">Read more</a>
    </div>
    <div class="welcome__divider"></div>
    <div class="features">
      <div class="feature">
        <div class="feature__icon"><svg viewBox="0 0 10 10"><rect x="1" y="2.5" width="8" height="5" rx=".6" fill="none" stroke="#e8923a" stroke-width=".8"/><circle cx="5" cy="5" r="1.3" fill="none" stroke="#e8923a" stroke-width=".7"/></svg></div>
        <div><div class="feature__title">Affordable</div><div class="small">Fair pricing for every session</div></div>
      </div>
      <div class="feature">
        <div class="feature__icon"><svg viewBox="0 0 10 10"><path d="M2 5.2 4.2 7.4 8 2.8" fill="none" stroke="#5bb04a" stroke-width="1.3"/></svg></div>
        <div><div class="feature__title">Permanent</div><div class="small">Results that stay for years</div></div>
      </div>
      <div class="feature">
        <div class="feature__icon"><svg viewBox="0 0 10 10"><circle cx="5" cy="5" r="3" fill="#4aa3df"/><circle cx="5" cy="5" r="1.1" fill="#fff"/></svg></div>
        <div><div class="feature__title">Guaranteed</div><div class="small">Satisfaction on every treatment</div></div>
      </div>
    </div>
  </section>

  <section class="services">
    <div class="services__bg" role="img" aria-label="Dark close-up of a gloved practitioner working on a client's scalp"></div>
    <h2 class="heading services__title">What we do</h2>
    <div class="dotline services__rule"><b></b><i></i><i></i><i></i><i></i><i></i><i></i><b></b></div>
    <div class="service-list">
      <div class="service"><div class="service__mark"></div><div class="dotline service__dots"><i></i><i></i><i></i><i></i><i></i><i></i></div><div class="service__name">Hairline</div></div>
      <div class="service"><div class="service__mark"></div><div class="dotline service__dots"><i></i><i></i><i></i><i></i><i></i><i></i></div><div class="service__name">Scar Camouflage</div></div>
      <div class="service"><div class="service__mark"></div><div class="dotline service__dots"><i></i><i></i><i></i><i></i><i></i><i></i></div><div class="service__name">Pattern Baldness</div></div>
    </div>
  </section>

  <section class="transform">
    <div class="transform__frame"></div>
    <div class="transform__photo" role="img" aria-label="Back of a client's head, before and after treatment side by side">
      <span class="transform__label" style="left:10px">BEFORE</span>
      <span class="transform__label" style="right:10px">AFTER</span>
    </div>
    <div class="transform__text">
      <h2 class="heading">Transformations</h2>
      <p class="small">See real client results from first visit to final session. Each treatment is planned around your skin tone, head shape and the look you want to achieve.</p>
      <a class="btn btn--outline">Read more</a>
    </div>
  </section>

  <section class="testimonials">
    <h2 class="heading">Testimonials</h2>
    <div class="round-arrow" style="left:8px"><svg viewBox="0 0 3 4"><path d="M2.4.4.8 2l1.6 1.6" fill="none" stroke="#fff" stroke-width=".6"/></svg></div>
    <div class="round-arrow" style="right:8px"><svg viewBox="0 0 3 4"><path d="M.6.4 2.2 2 .6 3.6" fill="none" stroke="#fff" stroke-width=".6"/></svg></div>
    <div class="cards">
      <div class="card"><div class="card__avatar" role="img" aria-label="Client portrait photo"></div><p>Lovely studio, calm process and a result that looks completely natural. Highly recommended.</p><div class="card__name">Lena Ortiz</div><div class="stars"><svg viewBox="0 0 10 10"><path d="M5 .5 6.3 3.6 9.6 3.8 7 6 7.9 9.3 5 7.5 2.1 9.3 3 6 .4 3.8 3.7 3.6Z" fill="#f5c518"/></svg><svg viewBox="0 0 10 10"><path d="M5 .5 6.3 3.6 9.6 3.8 7 6 7.9 9.3 5 7.5 2.1 9.3 3 6 .4 3.8 3.7 3.6Z" fill="#f5c518"/></svg><svg viewBox="0 0 10 10"><path d="M5 .5 6.3 3.6 9.6 3.8 7 6 7.9 9.3 5 7.5 2.1 9.3 3 6 .4 3.8 3.7 3.6Z" fill="#f5c518"/></svg><svg viewBox="0 0 10 10"><path d="M5 .5 6.3 3.6 9.6 3.8 7 6 7.9 9.3 5 7.5 2.1 9.3 3 6 .4 3.8 3.7 3.6Z" fill="#f5c518"/></svg><svg viewBox="0 0 10 10"><path d="M5 .5 6.3 3.6 9.6 3.8 7 6 7.9 9.3 5 7.5 2.1 9.3 3 6 .4 3.8 3.7 3.6Z" fill="#f5c518"/></svg></div></div>
      <div class="card"><div class="card__avatar" role="img" aria-label="Client portrait photo"></div><p>Lovely studio, calm process and a result that looks completely natural. Highly recommended.</p><div class="card__name">Marta Vale</div><div class="stars"><svg viewBox="0 0 10 10"><path d="M5 .5 6.3 3.6 9.6 3.8 7 6 7.9 9.3 5 7.5 2.1 9.3 3 6 .4 3.8 3.7 3.6Z" fill="#f5c518"/></svg><svg viewBox="0 0 10 10"><path d="M5 .5 6.3 3.6 9.6 3.8 7 6 7.9 9.3 5 7.5 2.1 9.3 3 6 .4 3.8 3.7 3.6Z" fill="#f5c518"/></svg><svg viewBox="0 0 10 10"><path d="M5 .5 6.3 3.6 9.6 3.8 7 6 7.9 9.3 5 7.5 2.1 9.3 3 6 .4 3.8 3.7 3.6Z" fill="#f5c518"/></svg><svg viewBox="0 0 10 10"><path d="M5 .5 6.3 3.6 9.6 3.8 7 6 7.9 9.3 5 7.5 2.1 9.3 3 6 .4 3.8 3.7 3.6Z" fill="#f5c518"/></svg><svg viewBox="0 0 10 10"><path d="M5 .5 6.3 3.6 9.6 3.8 7 6 7.9 9.3 5 7.5 2.1 9.3 3 6 .4 3.8 3.7 3.6Z" fill="#f5c518"/></svg></div></div>
      <div class="card"><div class="card__avatar" role="img" aria-label="Client portrait photo"></div><p>Lovely studio, calm process and a result that looks completely natural. Highly recommended.</p><div class="card__name">Peter Glenn</div><div class="stars"><svg viewBox="0 0 10 10"><path d="M5 .5 6.3 3.6 9.6 3.8 7 6 7.9 9.3 5 7.5 2.1 9.3 3 6 .4 3.8 3.7 3.6Z" fill="#f5c518"/></svg><svg viewBox="0 0 10 10"><path d="M5 .5 6.3 3.6 9.6 3.8 7 6 7.9 9.3 5 7.5 2.1 9.3 3 6 .4 3.8 3.7 3.6Z" fill="#f5c518"/></svg><svg viewBox="0 0 10 10"><path d="M5 .5 6.3 3.6 9.6 3.8 7 6 7.9 9.3 5 7.5 2.1 9.3 3 6 .4 3.8 3.7 3.6Z" fill="#f5c518"/></svg><svg viewBox="0 0 10 10"><path d="M5 .5 6.3 3.6 9.6 3.8 7 6 7.9 9.3 5 7.5 2.1 9.3 3 6 .4 3.8 3.7 3.6Z" fill="#f5c518"/></svg><svg viewBox="0 0 10 10"><path d="M5 .5 6.3 3.6 9.6 3.8 7 6 7.9 9.3 5 7.5 2.1 9.3 3 6 .4 3.8 3.7 3.6Z" fill="#f5c518"/></svg></div></div>
    </div>
  </section>

  <section class="gallery">
    <h2 class="heading">Gallery</h2>
    <div class="round-arrow" style="left:8px"><svg viewBox="0 0 3 4"><path d="M2.4.4.8 2l1.6 1.6" fill="none" stroke="#777" stroke-width=".6"/></svg></div>
    <div class="round-arrow" style="right:8px"><svg viewBox="0 0 3 4"><path d="M.6.4 2.2 2 .6 3.6" fill="none" stroke="#777" stroke-width=".6"/></svg></div>
    <div class="gallery__row">
      <div class="gallery__item" role="img" aria-label="Client with shaved head, top view" style="background:linear-gradient(180deg,#e9e6e3,#c7a890 55%,#d8d3cf)"></div>
      <div class="gallery__item" role="img" aria-label="Smiling client in a white shirt" style="background:linear-gradient(160deg,#9dc3e2,#8a6450 55%,#e8e8e8)"></div>
      <div class="gallery__item" role="img" aria-label="Practitioner treating a client in the studio" style="background:linear-gradient(135deg,#6f8fa8,#c9b7a8 50%,#7a6a5e)"></div>
      <div class="gallery__item" role="img" aria-label="Close-up of a pigmented scalp" style="background:linear-gradient(180deg,#8a6552,#6a4c3c)"></div>
    </div>
  </section>

  <section class="contact">
    <div class="contact__photo" role="img" aria-label="Photo of a smiling client in a black t-shirt giving a thumbs up"></div>
    <h2 class="heading">Contact form</h2>
    <div class="form">
      <div class="form__row"><span class="field">First Name</span><span class="field">Last Name</span></div>
      <div class="form__row"><span class="field">Email</span><span class="field">Phone Number</span></div>
      <div class="form__row"><span class="field field--area">Comments</span></div>
      <span class="form__submit">Submit</span>
    </div>
  </section>

  <footer class="site-footer">
    <div class="social"><span></span><span></span><span></span><span></span></div>
    <div class="footer__contact">
      <span><svg viewBox="0 0 10 10"><path d="M5 .5C3 .5 1.8 2 1.8 3.8 1.8 6.2 5 9.5 5 9.5S8.2 6.2 8.2 3.8C8.2 2 7 .5 5 .5Z" fill="#4aa3df"/></svg>Linden, OR 97000, United States</span><span>|</span>
      <span><svg viewBox="0 0 10 10"><path d="M2 1h2l1 2.5-1.3 1a6 6 0 0 0 2.8 2.8l1-1.3L10 7v2H8A8 8 0 0 1 1 2Z" fill="#4aa3df"/></svg>1 800 555 0142</span><span>|</span>
      <span><svg viewBox="0 0 10 10"><rect x="1" y="2" width="8" height="6" fill="#4aa3df"/><path d="M1 2 5 5.5 9 2" fill="none" stroke="#fff" stroke-width=".8"/></svg>hello@kdv-studio.com</span>
    </div>
    <div class="footer__links"><span>Help</span><span>|</span><span>FAQ</span><span>|</span><span>Support</span><span>|</span><span>Sitemap</span><span>|</span><span>Terms Of Use</span><span>|</span><span>Privacy Statement</span></div>
    <div class="copyright">Copyright © 2018. Scalp Micro Pigmentation. All rights reserved.</div>
  </footer>
</div>

<div class="page page--faq">
  <header class="site-header">
    <div class="logo"><span class="logo__name">KDV</span><span class="logo__by">BY MOIRA TALLOW</span></div>
    <nav class="nav">
      <a class="is-active">Home</a><a>About</a><a>Treatments</a><a>Gallery</a><a>Training</a><a>Transformations</a><a>Blog</a><a>Contact</a>
      <svg viewBox="0 0 10 10"><circle cx="4" cy="4" r="3" fill="none" stroke="#222" stroke-width="1.6"/><line x1="6.2" y1="6.2" x2="9" y2="9" stroke="#222" stroke-width="1.8"/></svg>
    </nav>
  </header>

  <section class="hero hero--short">
    <div class="hero__photo" role="img" aria-label="Man with a shaved head looking down, showing a defined hairline"></div>
    <div class="hero__arrow" style="left:0"><svg viewBox="0 0 4 6"><path d="M3 0.5 1 3 3 5.5" fill="none" stroke="#fff" stroke-width=".9"/></svg></div>
    <div class="hero__arrow" style="right:0"><svg viewBox="0 0 4 6"><path d="M1 0.5 3 3 1 5.5" fill="none" stroke="#fff" stroke-width=".9"/></svg></div>
    <h1 class="hero__title hero__title--faq">FAQ</h1>
  </section>

  <section class="faq">
    <h2>FAQ</h2>
    <div class="faq__list">
      <div class="faq__item is-open"><span class="faq__toggle"><svg viewBox="0 0 6 6"><line x1="1" y1="3" x2="5" y2="3" stroke="#fff" stroke-width=".9"/></svg></span>At vero eos et accusamus et iusto odio dignissimos ducimus qui blanditiis?<div class="faq__answer">Nemo enim ipsam voluptatem quia voluptas sit aspernatur aut odit aut fugit, sed quia consequuntur magni dolores eos.</div></div>
      <div class="faq__item"><span class="faq__toggle"><svg viewBox="0 0 6 6"><path d="M1 3h4M3 1v4" stroke="#fff" stroke-width=".9"/></svg></span>At vero eos et accusamus et iusto odio dignissimos ducimus qui blanditiis?</div>
      <div class="faq__item"><span class="faq__toggle"><svg viewBox="0 0 6 6"><path d="M1 3h4M3 1v4" stroke="#fff" stroke-width=".9"/></svg></span>At vero eos et accusamus et iusto odio dignissimos ducimus qui blanditiis?</div>
      <div class="faq__item"><span class="faq__toggle"><svg viewBox="0 0 6 6"><path d="M1 3h4M3 1v4" stroke="#fff" stroke-width=".9"/></svg></span>At vero eos et accusamus et iusto odio dignissimos ducimus qui blanditiis?</div>
      <div class="faq__item"><span class="faq__toggle"><svg viewBox="0 0 6 6"><path d="M1 3h4M3 1v4" stroke="#fff" stroke-width=".9"/></svg></span>At vero eos et accusamus et iusto odio dignissimos ducimus qui blanditiis?</div>
      <div class="faq__item"><span class="faq__toggle"><svg viewBox="0 0 6 6"><path d="M1 3h4M3 1v4" stroke="#fff" stroke-width=".9"/></svg></span>At vero eos et accusamus et iusto odio dignissimos ducimus qui blanditiis?</div>
      <div class="faq__item"><span class="faq__toggle"><svg viewBox="0 0 6 6"><path d="M1 3h4M3 1v4" stroke="#fff" stroke-width=".9"/></svg></span>At vero eos et accusamus et iusto odio dignissimos ducimus qui blanditiis?</div>
      <div class="faq__item"><span class="faq__toggle"><svg viewBox="0 0 6 6"><path d="M1 3h4M3 1v4" stroke="#fff" stroke-width=".9"/></svg></span>At vero eos et accusamus et iusto odio dignissimos ducimus qui blanditiis?</div>
      <div class="faq__item"><span class="faq__toggle"><svg viewBox="0 0 6 6"><path d="M1 3h4M3 1v4" stroke="#fff" stroke-width=".9"/></svg></span>At vero eos et accusamus et iusto odio dignissimos ducimus qui blanditiis?</div>
      <div class="faq__item"><span class="faq__toggle"><svg viewBox="0 0 6 6"><path d="M1 3h4M3 1v4" stroke="#fff" stroke-width=".9"/></svg></span>At vero eos et accusamus et iusto odio dignissimos ducimus qui blanditiis?</div>
      <div class="faq__item"><span class="faq__toggle"><svg viewBox="0 0 6 6"><path d="M1 3h4M3 1v4" stroke="#fff" stroke-width=".9"/></svg></span>At vero eos et accusamus et iusto odio dignissimos ducimus qui blanditiis?</div>
      <div class="faq__item"><span class="faq__toggle"><svg viewBox="0 0 6 6"><path d="M1 3h4M3 1v4" stroke="#fff" stroke-width=".9"/></svg></span>At vero eos et accusamus et iusto odio dignissimos ducimus qui blanditiis?</div>
      <div class="faq__item"><span class="faq__toggle"><svg viewBox="0 0 6 6"><path d="M1 3h4M3 1v4" stroke="#fff" stroke-width=".9"/></svg></span>At vero eos et accusamus et iusto odio dignissimos ducimus qui blanditiis?</div>
    </div>
  </section>

  <section class="contact">
    <div class="contact__photo" role="img" aria-label="Photo of a smiling client in a black t-shirt giving a thumbs up"></div>
    <h2 class="heading">Contact form</h2>
    <div class="form">
      <div class="form__row"><span class="field">First Name</span><span class="field">Last Name</span></div>
      <div class="form__row"><span class="field">Email</span><span class="field">Phone Number</span></div>
      <div class="form__row"><span class="field field--area">Comments</span></div>
      <span class="form__submit">Submit</span>
    </div>
  </section>

  <footer class="site-footer site-footer--faq">
    <div class="social"><span></span><span></span><span></span><span></span></div>
    <div class="footer__contact">
      <span><svg viewBox="0 0 10 10"><path d="M5 .5C3 .5 1.8 2 1.8 3.8 1.8 6.2 5 9.5 5 9.5S8.2 6.2 8.2 3.8C8.2 2 7 .5 5 .5Z" fill="#4aa3df"/></svg>Linden, OR 97000, United States</span><span>|</span>
      <span><svg viewBox="0 0 10 10"><path d="M2 1h2l1 2.5-1.3 1a6 6 0 0 0 2.8 2.8l1-1.3L10 7v2H8A8 8 0 0 1 1 2Z" fill="#4aa3df"/></svg>1 800 555 0142</span><span>|</span>
      <span><svg viewBox="0 0 10 10"><rect x="1" y="2" width="8" height="6" fill="#4aa3df"/><path d="M1 2 5 5.5 9 2" fill="none" stroke="#fff" stroke-width=".8"/></svg>hello@kdv-studio.com</span>
    </div>
    <div class="footer__links"><span>Help</span><span>|</span><span>FAQ</span><span>|</span><span>Support</span><span>|</span><span>Sitemap</span><span>|</span><span>Terms Of Use</span><span>|</span><span>Privacy Statement</span></div>
    <div class="copyright">Copyright © 2018. Scalp Micro Pigmentation. All rights reserved.</div>
  </footer>
</div>

</body>
</html>
```